Flyer for spiritual retreat (yoga, meditation, reiki, raw food)

I would like a flyer to promote my upcoming retreat and a matching Facebook banner.

The name of the retreat is "Wavecrest Of Calm" and the tagline is "retreat into you"

The activities in the retreat include daily meditation, ecstatic dance, spiritual development workshops on intuition, energy healing etc and a reiki session is included.

I would like a flyer designed to promote this, something that is editable as I will be running this multiple times and will need to adjust the flyer to add the dates etc each time.

edit: add that here will be fully catered raw food and juices, and that the retreat price includes all accomodation, meals and workshops.

Please contact me if you need further info. Please also visit my website www.marithovland.com and www.facebook.com/tolvanahaven to see my current events and promotions.

Thank you,

Marit

Reason: Hi all, thank you all for your submissions. Apologies as I am traveling and do not have much access to internet and will review your submissions and provide feedback as soon as possible. Kind regards, Marit.

Target Market(s)

People who like meditation, yoga, fans of rowan mabry and jasper vinek, those interested in personal and spiritual development.

Industry/Entity Type

Health And Wellness

Requirements
Must have
• Please put the included reiki session as as added bonus. Something like "BONUS 30 minute reiki healing session" in a little star/banner/something that stands out.
• Please emphasise the "light" part of Wavecrest as I am going for a play on words between in the light and enlightenment.
• Please include placeholder text for place, location, time
• Placeholder for price
• My name (see attached file - can change colour to suit) and website (www.marithovland.com)
Nice to have
• I prefer rounded designs, curves rather than block designs.
Should not have
• Tolvana Haven logo

```html
<!DOCTYPE html>
<html lang="en">
<head>
<meta charset="UTF-8">
<title>Wavecrest Of Calm – Retreat Into You</title>
<link rel="stylesheet" href="https://fonts.googleapis.com/css2?family=Playfair+Display:wght@400&family=Montserrat:wght@400;500&family=Open+Sans:wght@400;600&family=Great+Vibes&display=swap">
<style>
  :root {
    --violet-deep: #5a0f8c;
    --violet-mid: #7a22b0;
    --violet-glow: #b36bd8;
    --white: #ffffff;
    --gold: #f2b544;
    --light-glow: rgba(255, 236, 180, 0.85);
    --photo-blue: #3b3ea8;
    --photo-skin: #d9a98a;
    --photo-green: #7f8c5a;
  }
  * { margin: 0; padding: 0; box-sizing: border-box; }
  html, body { width: 848px; height: 1200px; overflow: hidden; }
  body { background: var(--violet-deep); }

  .flyer {
    position: relative;
    width: 848px;
    height: 1200px;
    overflow: hidden;
    background: radial-gradient(ellipse 520px 520px at 424px 650px, var(--violet-glow) 0%, var(--violet-mid) 45%, var(--violet-deep) 100%);
    color: var(--white);
    text-align: center;
  }

  .wreath {
    position: absolute;
    left: 142px;
    top: 45px;
    width: 564px;
    height: 564px;
    border-radius: 50%;
    background: rgba(255, 255, 255, 0.14);
  }
  .portrait {
    position: absolute;
    left: 204px;
    top: 107px;
    width: 440px;
    height: 440px;
    border-radius: 50%;
    border: 3px solid var(--white);
    background:
      radial-gradient(circle at 40% 55%, var(--photo-skin) 0%, rgba(217,169,138,0) 35%),
      linear-gradient(120deg, var(--photo-green) 0%, var(--photo-blue) 55%, #25278a 100%);
  }

  .title {
    position: absolute;
    top: 636px;
    left: 0;
    width: 100%;
    font-family: "Playfair Display", serif;
    font-weight: 400;
    font-size: 56px;
    line-height: 1.2;
  }
  .title-light {
    text-shadow: 0 0 14px var(--light-glow), 0 0 30px var(--light-glow);
  }
  .tagline {
    position: absolute;
    top: 720px;
    left: 0;
    width: 100%;
    font-family: "Montserrat", sans-serif;
    font-size: 20px;
    letter-spacing: 6px;
    color: var(--gold);
  }
  .description {
    position: absolute;
    top: 760px;
    left: 172px;
    width: 504px;
    font-family: "Open Sans", sans-serif;
    font-size: 15.6px;
    line-height: 20.5px;
    text-align: left;
  }

  .activities {
    position: absolute;
    top: 888px;
    left: 112px;
    width: 624px;
    font-family: "Open Sans", sans-serif;
    font-size: 13.5px;
    line-height: 18px;
    color: var(--gold);
  }
  .details {
    position: absolute;
    top: 926px;
    left: 0;
    width: 100%;
    font-family: "Montserrat", sans-serif;
    font-weight: 500;
    font-size: 13.5px;
    letter-spacing: 0.5px;
  }

  .divider {
    position: absolute;
    left: 369px;
    width: 110px;
    height: 10px;
    border-radius: 5px;
    background: var(--gold);
    opacity: 0.85;
  }
  .divider--top { top: 958px; }
  .divider--bottom { top: 1026px; }

  .bonus {
    position: absolute;
    top: 977px;
    left: 0;
    width: 100%;
    font-family: "Playfair Display", serif;
    font-size: 23px;
    color: var(--gold);
  }

  .signature {
    position: absolute;
    top: 1072px;
    left: 0;
    width: 100%;
    font-family: "Great Vibes", cursive;
    font-size: 42px;
    line-height: 1.2;
  }
  .signature-rule {
    position: absolute;
    top: 1146px;
    left: 332px;
    width: 186px;
    height: 1px;
    background: var(--white);
  }
  .website {
    position: absolute;
    top: 1153px;
    left: 0;
    width: 100%;
    font-family: "Open Sans", sans-serif;
    font-size: 16px;
  }
</style>
</head>
<body>
  <main class="flyer">
    <div class="wreath" role="img" aria-label="White floral wreath ornament framing the portrait"></div>
    <div class="portrait" role="img" aria-label="Photo of a woman in a blue top with hands pressed together in prayer, wearing layered necklaces"></div>

    <h1 class="title">Wave<span class="title-light">crest</span> Of Calm</h1>
    <p class="tagline">RETREAT INTO YOU</p>

    <p class="description">During these meditations you will be guided into a state of deep relaxation using a variety of techniques including breathwork, mindfulness meditation, visualisation and more. Sessions last up to 90 minutes. Approximately one hour is spent in meditation, often through a series of small meditations with a few minutes break in between each visualisation.</p>

    <p class="activities">Daily meditation · Ecstatic dance · Workshops on intuition &amp; energy healing<br>Fully catered raw food &amp; juices</p>
    <p class="details">[Date] · [Time] · [Venue, Location] &nbsp;|&nbsp; [Price] incl. all accommodation, meals &amp; workshops</p>

    <div class="divider divider--top" role="img" aria-label="Small gold laurel ornament"></div>
    <p class="bonus">"Bonus: 30 minute reiki healing session"</p>
    <div class="divider divider--bottom" role="img" aria-label="Small gold laurel ornament"></div>

    <p class="signature">Marit Hovland</p>
    <div class="signature-rule"></div>
    <p class="website">www.marithovland.com</p>
  </main>
</body>
</html>
```